Quorvane - corporate Business Card

We need a good look and innovative business card for a new start up company based in Los Angeles called "Quorvane". We are in a payment business, including payment card, app, and ewallet. We are expert in online payment and Card not present (CNP) transaction.
We need an innovative, modern business card.

Our logo font is Aero Matics

Target Market(s)

Startup - Bank - Online Payment - Card Manufacturing

Industry/Entity Type

Startup

Contact Information for Business Card

phone: 424 555 0173 - Address: 4270 Marbrook blvd, Dunhaven City, CA 90418

Requirements
Must have
• Message: innovative, professional, expert, high tech, trust, online payment expert, security
Nice to have
• no comment
Should not have
• no Comment

```html
<!DOCTYPE html>
<html lang="en">
<head>
<meta charset="utf-8">
<title>Quorvane – Business Card</title>
<link rel="stylesheet" href="https://fonts.googleapis.com/css2?family=Ubuntu:wght@500&family=Open+Sans:wght@400;600&display=swap">
<style>
  :root {
    --brand-red: #cf2640;
    --brand-red-dark: #b81d35;
    --band-grey: #b4b4b4;
    --card-white: #f7f7f7;
    --ink-white: #ffffff;
    --stage: #e8e5e0;
  }
  * { box-sizing: border-box; margin: 0; padding: 0; }
  html, body { width: 1200px; height: 780px; overflow: hidden; }
  body {
    background: var(--stage);
    font-family: "Open Sans", sans-serif;
    position: relative;
  }
  .card {
    position: absolute;
    top: 235px;
    width: 540px;
    height: 310px;
    overflow: hidden;
    box-shadow: 0 6px 18px rgba(0,0,0,.18);
  }
  .card--front { left: 30px; background: var(--card-white); }
  .card--back  { left: 630px; }

  /* Front */
  .front__brand {
    position: absolute;
    left: 34px; top: 42px;
    display: flex; align-items: center; gap: 16px;
  }
  .front__brand-dot {
    width: 70px; height: 70px; border-radius: 50%;
    background: var(--brand-red);
  }
  .front__brand-name {
    font-family: "Ubuntu", sans-serif;
    font-weight: 500;
    font-size: 54px;
    letter-spacing: -1px;
    color: var(--brand-red);
    line-height: 1;
  }
  .front__band {
    position: absolute; left: 0; right: 0; top: 150px; height: 28px;
    background: var(--band-grey);
    color: var(--ink-white);
    font-size: 14px;
    line-height: 28px;
    padding-left: 34px;
  }
  .front__band .person { font-weight: 600; font-size: 16px; }
  .front__band .divider { margin: 0 4px; opacity: .8; }
  .front__panel {
    position: absolute; left: 0; right: 0; top: 178px; bottom: 0;
    background: linear-gradient(180deg, var(--brand-red), var(--brand-red-dark));
    color: var(--ink-white);
    padding: 14px 34px;
    font-size: 13px;
    line-height: 19px;
  }
  .contact-line { display: flex; align-items: center; gap: 6px; }
  .contact-line svg { width: 14px; height: 14px; flex: none; }
  .address { margin-bottom: 6px; }
  .front__disc {
    position: absolute;
    left: 390px; top: 30px;
    width: 164px; height: 164px; border-radius: 50%;
    background: var(--brand-red);
    border: 8px solid var(--card-white);
  }

  /* Back */
  .card--back .back__field {
    position: absolute; inset: 0;
    background: radial-gradient(ellipse at 40% 40%, #d8304a 0%, var(--brand-red) 45%, var(--brand-red-dark) 100%);
  }
  .back__name {
    position: absolute; inset: 0;
    display: flex; align-items: center; justify-content: center;
    font-family: "Ubuntu", sans-serif;
    font-weight: 500;
    font-size: 66px;
    letter-spacing: -1px;
    color: var(--ink-white);
  }
</style>
</head>
<body>

<section class="card card--front" aria-label="Business card front">
  <div class="front__brand">
    <span class="front__brand-dot" aria-hidden="true"></span>
    <span class="front__brand-name">Quorvane</span>
  </div>
  <div class="front__band">
    <span class="person">Daniel Reyes</span><span class="divider">|</span><span class="role">Managing Director</span>
  </div>
  <div class="front__panel">
    <p class="address">4270 Marbrook blvd,<br>Dunhaven City, CA 90418</p>
    <p class="contact-line">
      <svg viewBox="0 0 14 14" aria-hidden="true"><rect width="14" height="14" rx="1" fill="#fff"/><path d="M4 3.2l1.6-.4.9 2.1-1 .8a6 6 0 0 0 2.8 2.8l.8-1 2.1.9-.4 1.6c-3.6.2-7-3.2-6.8-6.8z" fill="#cf2640"/></svg>
      <span>424 555 0173</span>
    </p>
    <p class="contact-line">
      <svg viewBox="0 0 14 14" aria-hidden="true"><rect width="14" height="14" rx="1" fill="#fff"/><rect x="2.5" y="4" width="9" height="6.5" fill="none" stroke="#cf2640" stroke-width="1.1"/><path d="M2.5 4l4.5 3.6L11.5 4" fill="none" stroke="#cf2640" stroke-width="1.1"/></svg>
      <span>hello@quorvane.co</span>
    </p>
  </div>
  <div class="front__disc" aria-hidden="true"></div>
</section>

<section class="card card--back" aria-label="Business card back">
  <div class="back__field" role="img" aria-label="Red field with a faint geometric texture"></div>
  <div class="back__name">Quorvane</div>
</section>

</body>
</html>
```